" Window Blinds and Shutters Business Card Design"

We require a business card design for a new windows blinds and shutters company based in Sydney.
The business name is 'Larkvale Blinds and Shutters'.
We supply and install homes and businesses with internal and external window furnishings and finishes. This includes varieties of window blinds and window shutters.

Benefits of Larkvale Blinds and Shutters :
Added security and privacy,
The ability to control the amount of sunlight,
Regulate internal temperature.

Blinds varieties:
Roller Blinds, Double Roller Blinds, Roman Blinds, Vertical Blinds, Aluminium venetians, Timber venetians and PVC Venetians.

Shutters varieties:
Plantation Shutters, Aluminium Louvre Shutters, Roller Shutters and Security Shutters .
Updates

Hi Designers,

Please have a look at my Business card design brief. I need your help to start my new business.

Thanks,

Dorian.

Reason: not 100% happy with the options available, close to 90% happy, need a little more refinement. Thank You & Good Luck

Target Market(s)

Home owners, business owners, shift workers , and new home builders.

Industry/Entity Type

Security

Contact Information for Business Card

Larkvale Blinds and Shutters,

Dorian Kettlewell mobile: 0487561904,
Priya Hensworth mobile: 0472846015,

email: dorian.kettlewell@mailgrove.net
web: larkvaleblindsandshutters.com.au

Colors
ffffff
9d9d9d
f78f20

Requirements
Must have
• ON FRONT OF CARD
I have attached a picture of logo and need a designer to design a font logo for Larkvale Blinds and Shutters similar, or open to suggestions.

FRONT OF CARD
Company message/:
"Shading every window with care"

BACK OF CARD
'For a FREE measure & quote call Dorian - 0487561904"
Nice to have
• Elegant yet professional.

Soft colours appealing to both male & female clients.

Should not have

• Unprofessional fonts

```html
<!DOCTYPE html>
<html lang="en">
<head>
<meta charset="utf-8">
<title>Larkvale Blinds and Shutters – Business Card</title>
<link href="https://fonts.googleapis.com/css2?family=Arimo:wght@400;700&display=swap" rel="stylesheet">
<style>
  :root {
    --stage: #d9d9d9;
    --card: #ffffff;
    --ink: #111111;
    --ink-soft: #333333;
    --brand-red: #ee2429;
    --brand-blue: #0a56a8;
    --pill-blue: #0b57a4;
  }
  * { box-sizing: border-box; margin: 0; padding: 0; }
  html, body {
    width: 1200px; height: 960px; overflow: hidden;
    background: var(--stage);
    font-family: "Arimo", Arial, sans-serif;
  }
  .canvas { position: relative; width: 1200px; height: 960px; }

  .card {
    position: absolute;
    background: var(--card);
    border-radius: 16px;
    box-shadow: 4px 5px 6px rgba(0,0,0,0.45);
    overflow: hidden;
  }
  .card--front { left: 54px; top: 50px; width: 606px; height: 368px; }
  .card--back  { left: 356px; top: 452px; width: 682px; height: 412px; }

  /* Wordmark */
  .wordmark { display: flex; align-items: center; gap: 12px; color: var(--ink-soft); font-weight: 400; }
  .wordmark__dot { width: 16px; height: 16px; border-radius: 50%; background: var(--brand-red); flex: none; }
  .wordmark__name { line-height: 1.05; }
  .wordmark__name span { display: block; }

  .card--front .wordmark {
    position: absolute; left: 0; right: 0; top: 160px; justify-content: center;
  }
  .card--front .wordmark__name { font-size: 36px; text-align: center; }
  .card--front .wordmark__name span + span { font-size: 22px; }
  .tagline {
    position: absolute; left: 0; right: 0; top: 234px;
    text-align: center; color: var(--brand-red); font-size: 12px;
  }

  /* Back */
  .partners { position: absolute; left: 0; top: 17px; width: 162px; }
  .partner {
    height: 26px; margin-bottom: 5px;
    background: var(--pill-blue); color: #fff;
    border-radius: 0 13px 13px 0;
    font-size: 14px; line-height: 26px; text-align: center;
  }
  .partner__first { color: var(--brand-red); }
  .partners__role {
    margin-top: 5px; padding-left: 25px;
    font-size: 14px; font-weight: 400; color: var(--ink); letter-spacing: 0.2px;
  }

  .card--back .wordmark { position: absolute; left: 30px; top: 198px; }
  .card--back .wordmark__name { font-size: 26px; }
  .card--back .wordmark__name span + span { font-size: 15px; }

  .divider {
    position: absolute; left: 335px; top: 148px; width: 3px; height: 122px;
    background: linear-gradient(to bottom, transparent, var(--brand-red) 50%, transparent);
  }

  .contacts { position: absolute; left: 365px; top: 160px; list-style: none; }
  .contact { display: flex; align-items: center; gap: 9px; height: 31px; font-size: 14.5px; color: var(--ink); }
  .contact__icon {
    width: 20px; height: 20px; border-radius: 3px; background: var(--pill-blue);
    display: flex; align-items: center; justify-content: center; flex: none;
  }

  .cta {
    position: absolute; left: 0; right: 0; top: 340px;
    text-align: center; font-size: 16.5px; color: var(--brand-blue);
  }
  .rule-blue { position: absolute; left: 0; right: 0; top: 373px; height: 5px; background: var(--brand-blue); }
  .band-red  { position: absolute; left: 0; right: 0; top: 382px; bottom: 0; background: var(--brand-red); }
</style>
</head>
<body>
<main class="canvas">

  <section class="card card--front" aria-label="Card front">
    <div class="wordmark">
      <span class="wordmark__dot"></span>
      <p class="wordmark__name"><span>Larkvale</span><span>Blinds and Shutters</span></p>
    </div>
    <p class="tagline">"Shading every window with care"</p>
  </section>

  <section class="card card--back" aria-label="Card back">
    <div class="partners">
      <p class="partner"><span class="partner__first">Dorian</span> Kettlewell</p>
      <p class="partner"><span class="partner__first">Priya</span> Hensworth</p>
      <p class="partners__role">Business Partners</p>
    </div>

    <div class="wordmark">
      <span class="wordmark__dot"></span>
      <p class="wordmark__name"><span>Larkvale</span><span>Blinds and Shutters</span></p>
    </div>

    <div class="divider"></div>

    <ul class="contacts">
      <li class="contact">
        <span class="contact__icon">
          <svg width="10" height="14" viewBox="0 0 10 14"><rect x="1" y="0.5" width="8" height="13" rx="1.5" fill="none" stroke="#ee2429" stroke-width="1.4"/><circle cx="5" cy="11" r="0.9" fill="#ee2429"/></svg>
        </span>0487561904
      </li>
      <li class="contact">
        <span class="contact__icon">
          <svg width="14" height="10" viewBox="0 0 14 10"><rect width="14" height="10" fill="#ee2429"/><path d="M0 0 L7 6 L14 0" fill="none" stroke="#0b57a4" stroke-width="1"/></svg>
        </span>dorian.kettlewell@mailgrove.net
      </li>
      <li class="contact">
        <span class="contact__icon">
          <svg width="14" height="14" viewBox="0 0 14 14" fill="none" stroke="#ee2429" stroke-width="1.2"><circle cx="7" cy="7" r="6"/><ellipse cx="7" cy="7" rx="2.6" ry="6"/><path d="M1 7h12M2 4h10M2 10h10"/></svg>
        </span>larkvaleblindsandshutters.com.au
      </li>
    </ul>

    <p class="cta">Call 0487561904 for a free measure and quote!'</p>
    <div class="rule-blue"></div>
    <div class="band-red"></div>
  </section>

</main>
</body>
</html>
```